Berichtslayout für Unternehmensberatung mit Schwerpunkt Softwareentwicklung für den Public Sektor
Wir sind eine Unternehmensberatung, die sich auf Softwareentwicklung für den Public Sektor spezialisiert hat (www.tqm-beratung.de). Unsere Zielgruppe sind Verwaltungen im deutschsprachigen Raum. Wir bieten für diesen Markt verschiedene Softwareprodukte an. Aus unseren Softwareprodukten werden automatische Controllingberichte erzeugt.
Company
We are a consulting company, that is specialised in softwaredevelopment regarding the public sector (www.tqm-beratung.de). Our customers are administrations all over Germany, Austria and Swiss. We offer different products to the market. One of which produces a report you can find enclosed to this project.
Aufgabenstellung
Es soll ein Berichtslayout erstellt werden.
• Das Berichtslayout muss die Informationen des Berichtsentwurfs aufnehmen können, beispielsweise Tabellen etc. (Anlage 1)
• Der Bericht enthält viel Text und viele Zahlen, weshalb auch ein Vorschlag über die Gestaltung der Tabellen enthalten sein soll. (Anlage 1)
• Das Layout kann Symbole wie den Falkmoorer Zeichen oder die Farben des Deckblatts aufnehmen (Anlage 2). Alle anderen Elemente können verändert werden.
• Schriftart muss Calibri sein.
• Das Berichtslayout soll übersichtlich und ansprechend aussehen.
• Das Berichtslayout soll, soweit möglich, nicht überladen wirken.
Der Bericht wird über jasper Reports erzeugt.
Wenn das Design in AI oder Indesign entwickelt wird, sollten wir dies verwenden können.
Task:
We need a better Layout for our report.
• The Layout has to be able to handle the informations shown in 'Anlage 1'.
• The layout can use Symbols like the 'Falkmoorer Zeichen' (Falkmoorer Sign) or colors of the covering page shown in 'Anlage 2'.
• Since the Layout has to handle a lot of numbers an text it would be nice if you could deliver a layout suggestion for those elements as well
• The Font has to be Calibri
• The Layout sould look as clean and appealing as possible.

```html
<!DOCTYPE html>
<html lang="de">
<head>
<meta charset="utf-8">
<title>Controlling 01-06/19 – 07 Inneres</title>
<link href="https://fonts.googleapis.com/css2?family=Carlito:wght@400;700&family=Open+Sans:wght@600;700&display=swap" rel="stylesheet">
<style>
:root{
  --red:#d01317;
  --ink:#3a3a3a;
  --bg:#f2f2f2;
  --paper:#ffffff;
  --grid:#9a9a9a;
  --head:#e4e4e4;
  --ok:#3aa935;
  --warn:#f5c400;
}
*{margin:0;padding:0;box-sizing:border-box}
html,body{width:880px;height:1200px;overflow:hidden;background:var(--bg)}
body{position:relative;font-family:'Carlito',sans-serif;color:var(--ink)}
.page{position:absolute;width:379px;height:536px;background:var(--paper);box-shadow:2px 3px 6px rgba(0,0,0,.18);overflow:hidden}
.p39{left:57px;top:62px}
.p40{left:454px;top:62px}
.p41{left:57px;top:614px}
.block{position:absolute;left:23px;width:333px}
.banner{position:absolute;left:0;background:var(--red);color:#fff;font-family:'Open Sans',sans-serif;font-weight:700;letter-spacing:.4px;padding-left:23px;display:flex;flex-direction:column;justify-content:center}
.banner-short{top:23px;height:25px;width:112px;font-size:10px}
.banner-tall{top:21px;height:46px;width:197px;font-size:10px;line-height:15px}
.section-title{font-family:'Open Sans',sans-serif;font-weight:700;font-size:7.6px;color:#333;letter-spacing:.2px;display:inline-block}
.section-title::after{content:"";display:block;width:37px;height:.8px;background:var(--red);margin-top:2px}
.sub{color:var(--red);font-size:6.6px;margin-bottom:2px}
.text{font-size:6.5px;line-height:8.45px;text-align:justify;hyphens:auto}
.cols{column-count:2;column-gap:8px}
.gap{margin-top:8.45px}
ul.bul{list-style:none}
ul.bul li::before{content:"• ";color:var(--red)}
.footer{position:absolute;left:23px;width:333px;top:512px;border-top:.8px solid var(--red);padding-top:4px;font-size:5.8px;line-height:6px;display:flex;justify-content:space-between;align-items:flex-end}
.footer .num{font-size:6px}
.right{text-align:right}
ol.measures{list-style:none;font-size:6.5px;line-height:8.45px}
ol.measures li{display:flex;margin-bottom:2.5px;text-align:justify}
ol.measures b{color:var(--red);font-weight:400;width:5px;flex:none}
table{border-collapse:collapse;width:100%;font-size:4.2px;color:#222}
table.fin{border:.9px solid #444}
table td,table th{padding:0 2px;height:9px;text-align:right;font-weight:400;border-right:.5px dashed var(--grid)}
table thead th{background:var(--head);text-align:center;font-weight:700;border-bottom:.5px solid var(--grid)}
table thead tr.unit th{font-weight:400}
table .label{text-align:left;border-right:.9px solid #444}
table thead .label{text-align:center;font-size:5.2px}
table .sepcol{border-right:.9px solid #444}
tr.sum td{font-weight:700;border-top:.9px solid #444;border-bottom:.9px solid #444}
tr.tot td{font-weight:700}
.legend{font-size:6.4px;line-height:11px;display:grid;grid-template-columns:60px 92px 116px 80px}
.dot{display:inline-block;width:7px;height:7px;border-radius:50%;vertical-align:-1px;margin-right:3px}
table.kpi{border:.9px solid #444;font-size:4.4px}
table.kpi td{height:9px}
</style>
</head>
<body>

<section class="page p39">
  <div class="banner banner-short">KOMMENTAR</div>
  <div class="block" style="top:66px"><h2 class="section-title">FINANZDATEN</h2></div>

  <div class="block" style="top:89px">
    <div class="sub">PPL 07</div>
    <div class="text">
      <p>Der PPL 07 wird sein Budget nach gegenwärtigem Stand um 12,8 Mio. € überschreiten (Land: 5,9 Mio. €; Stadt: 6,9 Mio. €). Im Vergleich zum Controlling 01-05/2019 ergibt sich damit eine Verschlechterung in Höhe von 4,5 Mio. €. Die Verschlechterung setzt sich aus Folgenden Veränderungen zusammen:</p>
      <ul class="bul">
        <li>Erhöhung Mindereinnahmen um 2 Mio. € (Land: 1,7 + Stadt: 0,3)</li>
        <li>Reduzierung Personalmehrausgaben um 2 Mio. € (Land: -1,8; Stadt: -0,2)</li>
        <li>Erhöhung konsumtive Mehrausgaben um 3,2 Mio. € (Stadt: 3,2)</li>
        <li>Erhöhung investive Mehrausgaben um 1,3 Mio. € (Stadt: 1,3)</li>
      </ul>
    </div>
  </div>

  <div class="block" style="top:176px">
    <div class="sub">Konsumtive Einnahmen</div>
    <div class="text cols">
      <p>Bei den konsumtiven Einnahmen werden derzeit rd. 2,2 Mio. € an Mindereinnahmen prognostiziert.<br>Die Verschlechterung um ca. 2 Mio. € im Vergleich zum letzten Controlling entsteht insbesondere dadurch, dass die noch im Controlling 01-05/2019 ausgewiesenen Mehreinnahmen für Polizeieinsätze bei Hochrisiko-Fußballspielen von 1,5 Mio. € auf 1,2 Mio. € abgesenkt wurden. Im Controlling 01-04 ging man noch von Einnahmen in Höhe von 2 Mio. € aus.<br>Des Weiteren sollen laut Ressort – vorbehaltlich einer entsprechenden Gremienbefassung – die voraussichtlichen Einnahmen i. H. v. 1,2 Mio. € komplett für die Auszahlung von Überstunden bei der Polizei verwendet werden. Folglich wären sie dadurch nicht mehr als Mehreinnahmen vorhanden. Im Controlling 01-05 sollten dagegen bisher nur lediglich 0,5 Mio. € dafür verwendet werden. Gem. Haushaltsvermerk der entsprechenden Einnahme-Haushaltsstelle sind die Einnahmen allerdings bis maximal 0,5 Mio. € zur Auszahlung von Überstunden begrenzt. Es bleibt zudem abzuwarten, ob die Einnahmen überhaupt noch in 2019 eingehen.</p>
      <p class="gap">Des Weiteren haben sich die Mindereinnahmen bei den Gebühren für Feuerwehreinsätze um 0,4 Mio. € erhöht und es entstehen Mindereinnahmen in der Produktgruppe Wahlen in Höhe von 0,2 Mio. €. Laut Ressort wird die Kostenerstattung zur Wahl des europäischen Parlaments geringer ausfallen, da aufgrund der gleichzeitig durchgeführten Wahlen nicht alle Kosten abrechnungsfähig sind.<br>In den Produktgruppen im Bereich „Öffentliche Ordnung“ haben sich die Mindereinnahmen geringfügig von 0,262 Mio. € auf 0,17 Mio. € reduziert. Im Personalbereich werden im Vergleich zum Controlling 01-05/2019 ca. 2 Mio. € weniger Personalmehrausgaben ausgewiesen. Ursächlich ist dafür laut Ressort eine fälschlicherweise doppelte Berücksichtigung von Personaleinstellungen in der Polizei.</p>
    </div>
  </div>

  <div class="block" style="top:351px">
    <div class="sub">Konsumtive Ausgaben</div>
    <div class="text cols">
      <p>Bei den konsumtiven Ausgaben werden zum Jahresende derzeit 3,7 Mio. € an Mehrausgaben prognostiziert. Die Steigerung der Ausgaben im Vergleich zum Controlling 01-05/2019 i. H. v. 3,2 Mio. € ergibt sich insbesondere durch Mehrausgaben im Rettungsdienst. Laut Ressort liegt dies zum Großteil an den aus der Monatsabrechnung losgelösten Auszahlungen an Hilfsorganisationen. Des Weiteren stehen für den Bereich Notärzte noch Rechnungen aus. Die Jahreseinschätzung der Einsatzzahlen im Rettungsdienst liegt um circa 10% unter den JahresPlanwerten, dennoch entstehen Mehrausgaben.</p>
      <p class="gap">Zusätzlich zu den durch das beschlossene Kapazitätskonzept II entstehen Bedarfen für die zusätzliche Einstellung von Studierenden im Polizeivollzug prognostiziert die Polizei zusätzliche Mehrausgaben i. H. v. 1,2 Mio. € für Geschäftsbedarf und Digitalfunkgeräte (0,57 Mio. €), DNA- und BTM Fremdvergabe (0,270 Mio. €), Folgekosten von im Rahmen des Handlungsfeldes Sichere und Saubere Stadt erworbenen Schutzausstattungen (0,215 Mio. €) sowie Dolmetscherkosten (0,145 Mio. €). Diese Mehrbedarfe wurden im letzten Controlling 01-05/2019 nicht ausgewiesen. Es ist fraglich, weshalb diese Mehrbedarfe erst jetzt ausgewiesen werden.</p>
      <p class="gap">Dem gegenüber stehen dagegen konsumtive Minderausgaben im Umfang von 1,2 Mio. € aufgrund geringerer Ausgaben für die Bürgerschafts- und Beirätewahl sowie der Europawahl. Insbesondere die Druckkosten sind laut Ressort erheblich niedriger ausgefallen, als ursprünglich vom Ressort erwartet.</p>
    </div>
  </div>

  <footer class="footer">
    <span>Controlling 01-06/19<br>28.09.19</span>
    <span class="num">39</span>
    <span>07 Inneres</span>
  </footer>
</section>

<section class="page p40">
  <div class="block" style="top:24px">
    <div class="sub">Investive Ausgaben</div>
    <div class="text cols">
      <p>Bei den investiven Ausgaben werden Mehrausgaben im Umfang von 3,866 Mio. € prognostiziert. Im Vergleich zum letzten Controlling ergibt sich damit eine Verschlechterung i. H. v. rd. 1,3 Mio. €.<br>Die Verschlechterung tritt ausschließlich im Rettungsdienst auf und ist darauf zurückzuführen, dass die Rettungsdienst-Fahrzeuge nicht mehr über das Hilfswerk Nordstern beschafft und finanziert werden, sondern über den Haushalt beschafft werden. In der Gebührenkalkulation wird zudem nur rd. ein Fünftel des Betrages an Abschreibungen aufgenommen.</p>
      <p class="gap">Vor dem Hintergrund der dadurch entstehenden finanziellen Auswirkungen werden der Senator für Inneres in Abstimmung mit der Senatorin für Finanzen eine vertiefte Betrachtung der Entwicklung der investiven Ausgaben des Rettungsdienstes vornehmen. Dies beinhaltet die konkreten Planungen zur Fahrzeugbeschaffung sowie Berücksichtigung in der Gebührenkalkulation, zur Abfinanzierung der Alt-Fahrzeuge sowie die im Rahmen der Haushaltsaufstellung 2020/2021 durch den Senator für Inneres vorzunehmenden Anschlagsveränderungen.</p>
      <p class="gap">Des Weiteren fallen laut Ressort für das Projekt Mobile Datenerfassung rd. 2 Mio. € an Ausgaben an. Hier sollte seitens des Innenressorts geprüft werden, in wie weit diese Kosten im Rahmen der Gebührenkalkulation eingeflossen sind.</p>
      <p class="gap">Insgesamt entstehen damit in der Produktgruppe Rettungsdienst Mehrausgaben i.H.v. 1,8 Mio.€. Weiterhin entstehen die investiven Bedarfe durch das Kapazitätskonzept I und II bei der Polizei i.H.v. 2,066 Mio. €.</p>
    </div>
  </div>

  <div class="block" style="top:192px">
    <div class="sub">Finanzierungssaldo</div>
    <div class="text cols">
      <p>Der zulässige produktplanbezogene Finanzierungssaldo wird unter Berücksichtigung von produktplanübergreifenden Verlagerungen (ca. 25,6 Mio. €) um rd. 14,454 Mio. € (Land: 7,3 Mio. €; Stadt: 7,1 Mio. €) überschritten. Die Differenz zwischen der Budgetüberschreitung (12,8 Mio. €) und der Überschreitung des Finanzierungssaldos (14,454 Mio. €) lässt sich teilweise durch die aus 2018 übertragenen haushaltsmäßig nicht finanzierten Rücklagen im Bereich des Digitalfunks und der durch das Ressort dargestellten Inanspruchnahme (ohne Liquidität) dieser erklären. Die restliche Differenz in Höhe von rd. 1,6 Mio. € kann bisher durch das Ressort noch nicht aufgeklärt werden.</p>
    </div>
  </div>

  <div class="block" style="top:284px"><h2 class="section-title">PERSONALDATEN</h2></div>

  <div class="block" style="top:308px">
    <div class="text cols">
      <p>Im Produktplan 07 – Inneres – werden voraussichtliche Personalmehrausgaben in Höhe von rund 3,5 Mio. € erwartet. Dies korrespondiert mit einer vom Ressort geplanten erheblichen Überschreitung der Zielzahlen und Sollvorgaben zum Jahresende.<br>Die Mehrausgaben und Überschreitungen fallen ausschließlich im Land an und resultieren größtenteils aus geplanten bzw. bereits vollzogenen Neueinstellungen sowie auf umfangreiche Beförderungen in den letzten Jahren (Überschreitung Land: ca. 3,65 Mio. €, Unterschreitung Stadt: ca. 0,15 Mio. €).</p>
      <p class="gap">Gegenüber den Vormonaten weist der Produktplan 07 eine Verbesserung um rund 1,7 Mio. € aus. Ursächlich für die Differenz war eine doppelte Berücksichtigung von zukünftigen Personaleinstellungen in der Ressortprognose. Dabei wurden u.a. folgende Sollveränderungen berücksichtigt: Erwartete Nachbewilligungen bzw. Einsparungen für die Durchführung der Wahlen 2019, für die Aussteuerung der Ausbildungsplanung, für das Förderprogramm LOTSENPLUS und zum zentralen Ausgleich der Beihilfen und Nachversicherungen, Einnahmeverfügungsmittel zur Intensivierung der Gewinnabschöpfung und zur Teilfinanzierung von Fußballeinsätzen bei Problemspielen (FBZ) sowie sollmindernde Verbeamtungseffekte (in der Ressorthochrechnung nicht enthalten).</p>
      <p class="gap">Auf der Ausgabeseite wurden u.a. folgende Punkte im voraussichtlichen Ist berücksichtigt: Erwartete Personalausgaben aufgrund von Neueinstellungen im Kernbereich und bei den temporären Personalmitteln bzw. in den Handlungsfeldern, aufgrund von Übernahmen aus der Ausbildung bei der Polizei und bei der Feuerwehr, aufgrund von Auszahlungen von Überstunden (vgl. Einnahmen FBZ) und aufgrund der Rufbereitschaft der Einsatzdienste der Feuerwehr sowie die erwartete Restfluktuation und Zahlungen aufgrund der Altersteilzeitrückstellungen.</p>
      <p class="gap">Eine mögliche Problemlösung wird von Innenressort nicht aufgezeigt. Es ist ein restriktives personalwirtschaftliches Handeln erforderlich.</p>
    </div>
  </div>

  <footer class="footer">
    <span>07 Inneres</span>
    <span class="num">40</span>
    <span class="right">Controlling 01-06/19<br>28.09.19</span>
  </footer>
</section>

<section class="page p41">
  <div class="banner banner-tall">MASSNAHMEN-<br>STEUERUNGSVORSCHLAG</div>

  <div class="block" style="top:88px">
    <ol class="measures">
      <li><b>1</b><span>Das Ressort wird gebeten, die Höhe der Bedarfe aus den Kapazitätskonzepten I und II zu überprüfen und entsprechend des Beschlusses des Senats vom 30. April 2019 zunächst eine Lösung innerhalb des Produktplanbudgets sicherzustellen.</span></li>
      <li><b>2</b><span>Das Ressort wird gebeten, im Controlling 01-09/2019 die konsumtiven Mehrbedarfe der Polizei, ggfs. durch Mengengerüste, detaillierter darzustellen und zu erläutern, weshalb diese Bedarfe erstmalig im Controlling 01-06/2019 dargestellt wurden.</span></li>
      <li><b>3</b><span>Das Ressort wird gebeten, sämtliche Möglichkeiten zur Verbesserung der Einnahmen und zur Reduzierung der Ausgaben zu ergreifen um die Höhe der erwarteten Budgetrisiken zum Jahresende noch zu minimieren.</span></li>
    </ol>
  </div>

  <div class="block" style="top:189px"><h2 class="section-title">RESSOURCENEINSATZ</h2></div>

  <div class="block" style="top:212px">
    <table class="fin">
      <thead>
        <tr><th class="label" rowspan="3">Kamerale<br>Finanzdaten</th><th colspan="5" class="sepcol">Januar - Juni 2019</th><th colspan="4">Jahresplanung 2019</th></tr>
        <tr><th>Ist</th><th>Planwert</th><th colspan="2">Ist-Planwert Abweichung</th><th class="sepcol">HH-Soll</th><th>vor. HH-Soll</th><th>vor. Ist</th><th>Abweichung</th><th>Anschlag</th></tr>
        <tr class="unit"><th colspan="3">Tsd. EUR</th><th>%</th><th class="sepcol"></th><th colspan="4">Tsd. EUR</th></tr>
      </thead>
      <tbody>
        <tr><td class="label">Konsumtive Einnahmen</td><td>28.725</td><td>31.545</td><td>-2.819</td><td>-8,94</td><td class="sepcol">53.854</td><td>59.965</td><td>57.789</td><td>-2.176</td><td>58.126</td></tr>
        <tr><td class="label">Investive Einnahmen</td><td>36</td><td>19</td><td>17</td><td>86,62</td><td class="sepcol">49</td><td>49</td><td>84</td><td>35</td><td>48</td></tr>
        <tr><td class="label">Verrechnungen/Erstattungen (Einn)</td><td>6.333</td><td>5.577</td><td>755</td><td>13,54</td><td class="sepcol">9.255</td><td>9.318</td><td>9.318</td><td>0</td><td>9.313</td></tr>
        <tr><td class="label">&nbsp;- Land, Statgem. u. intern</td><td>6.332</td><td>5.577</td><td>755</td><td>13,53</td><td class="sepcol">9.253</td><td>9.254</td><td>9.254</td><td>0</td><td>9.248</td></tr>
        <tr><td class="label">&nbsp;- von Falkmoorhafen</td><td>1</td><td>0</td><td>1</td><td></td><td class="sepcol">2</td><td>64</td><td>64</td><td>0</td><td>64</td></tr>
        <tr class="sum"><td class="label">Budgetierte Einnahmen</td><td>35.094</td><td>37.142</td><td>-2.047</td><td>-5,51</td><td class="sepcol">63.158</td><td>69.332</td><td>67.191</td><td>-2.141</td><td>67.487</td></tr>
        <tr><td class="label">Personalausgeben</td><td>99.179</td><td>89.774</td><td>9.405</td><td>10,48</td><td class="sepcol">199.715</td><td>205.249</td><td>208.332</td><td>3.083</td><td>183.805</td></tr>
        <tr><td class="label">Zinsausgeben</td><td>0</td><td>11</td><td>-11</td><td>-100,0</td><td class="sepcol">23</td><td>23</td><td>23</td><td>0</td><td>34</td></tr>
        <tr class="sum"><td class="label">Budgetierte Ausgaben</td><td>166.008</td><td>156.339</td><td>9.669</td><td>6,18</td><td class="sepcol">322.361</td><td>330.588</td><td>341.254</td><td>10.666</td><td>301.484</td></tr>
        <tr class="tot"><td class="label">SALDO</td><td>-130.914</td><td>-119.197</td><td>-11.716</td><td>-9,83</td><td class="sepcol">-259.203</td><td>-261.256</td><td>-274.063</td><td>-12.807</td><td>-233.997</td></tr>
      </tbody>
    </table>
  </div>

  <div class="block" style="top:386px"><h2 class="section-title">STRATEGISCHE ZIELE / KENNZAHLEN / MENGENGERÜSTE</h2></div>

  <div class="block" style="top:412px">
    <div class="legend">
      <span>Steuerbarkeit:</span>
      <span><i class="dot" style="background:#444"></i>direkt steuerbar</span>
      <span><svg width="8" height="8" viewBox="0 0 8 8" style="vertical-align:-1px;margin-right:3px"><circle cx="4" cy="4" r="3.4" fill="#fff" stroke="#444" stroke-width=".8"/><path d="M4 .6A3.4 3.4 0 0 0 4 7.4Z" fill="#444"/></svg>eingeschränkt steuerbar</span>
      <span><i class="dot" style="border:.8px solid #444"></i>nicht steuerbar</span>
      <span>Zielerreichnung:</span>
      <span><i class="dot" style="background:var(--ok)"></i>nicht gefährdet</span>
      <span><svg width="8" height="7" viewBox="0 0 8 7" style="vertical-align:-1px;margin-right:3px"><path d="M4 0L8 7H0Z" fill="var(--warn)"/></svg>im Toleranzbereich</span>
      <span><i class="dot" style="background:var(--red)"></i>gefährdet</span>
    </div>
  </div>

  <div class="block" style="top:446px;width:320px">
    <table class="kpi">
      <thead>
        <tr><th class="label" rowspan="2">Kriminalitätsbekämpfung</th><th colspan="2">Januar- Juni 2019</th><th colspan="2">Ist-Plan Abweichung</th><th>2019</th><th rowspan="2">Steuer-<br>barkeit</th><th rowspan="2">Status</th></tr>
        <tr><th>Ist</th><th>Planwert</th><th>abs.</th><th>%</th><th>Planwert</th></tr>
      </thead>
      <tbody>
        <tr><td class="label" colspan="8" style="border-bottom:.5px solid var(--grid)">Leistungen</td></tr>
        <tr><td class="label">300242 Aufklärungsquote [%]</td><td>47,50</td><td>49,00</td><td>-1,50</td><td></td><td>49,00</td><td></td><td rowspan="2" style="text-align:center"><svg width="8" height="7" viewBox="0 0 8 7"><path d="M4 0L8 7H0Z" fill="var(--warn)"/></svg></td></tr>
        <tr><td class="label">300596 Anzahl straf. Ermittlungsverf. -gesamt- [Anz.]</td><td>38.003,000</td><td>44.250,000</td><td>-6.247,000</td><td>-14,12</td><td>88.500,000</td><td></td></tr>
      </tbody>
    </table>
  </div>

  <footer class="footer">
    <span>Controlling 01-06/19<br>28.09.19</span>
    <span class="num">41</span>
    <span>07 Inneres</span>
  </footer>
</section>

</body>
</html>
```